Solar Energy Company Overview Presentation

Hello designers,

Our company Vantrel Energy Solutions is looking to re-design our company overview presentation labeled "Statement of Qualifications". Currently this document is provided in .doc and .PDF formats to clients and partners.

We would like to keep a professional and clean look, while making it look more sleek and up to do date with more modern design standards. Please see attached document for the current layout.

In addition we would like to add a page for corporate leadership, that is not currently on the document. It will have a photo of team member, title, and bio.

This should be a template that can be edited in the future with Microsoft word if possible. We also have the capabilities to use Photoshop if needed.

I have attached our current document titled "Statement of Qualifications" so you can view the type of content that is on it. I also attached other marketing items so you can get an idea of how some of our other branding looks. I have also attached the font we like to use. Please feel free to take you own creative direction.

Our website is http://vantrelenergy-example.com

Thank you for your consideration, please message me with any questions.

Galen

Target Market(s)

Solar Industry Companies and Clients

Industry/Entity Type

It Company

Requirements
Must have
• Professional Design With Modern High-End Look

```html
<!DOCTYPE html>
<html lang="en">
<head>
<meta charset="utf-8">
<title>Vantrel Energy Solutions – Company Overview</title>
<link rel="stylesheet" href="https://fonts.googleapis.com/css2?family=Bebas+Neue&family=Oswald:wght@300;500&family=Raleway:wght@400;500;700;800&display=swap">
<style>
  :root{
    --orange:#e8701f;
    --orange-deep:#d9601a;
    --ink:#111111;
    --text:#3a3a3a;
    --paper:#f7f7f7;
    --stage:#eeeeee;
    --photo-sky:#8fa4b6;
    --photo-ground:#7d7a73;
  }
  *{box-sizing:border-box;margin:0;padding:0}
  html,body{width:1200px;height:846px;overflow:hidden;background:var(--stage)}
  body{position:relative;font-family:"Raleway",sans-serif;color:var(--text)}
  .page{position:absolute;top:26px;width:539px;height:762px;background:var(--paper);box-shadow:0 2px 10px rgba(0,0,0,.18);overflow:hidden}
  .page--cover{left:24px}
  .page--sheet{left:638px}
  .page__art{position:absolute;inset:0}
  .page__foot{position:absolute;left:0;right:0;bottom:0;height:14px;background:var(--orange-deep);border-top:3px solid #f0a060}
  .page-label{position:absolute;top:802px;font-family:"Raleway",sans-serif;font-size:24px;font-weight:500;color:var(--ink)}

  /* cover */
  .brand{position:absolute;left:28px;top:78px;display:flex;align-items:center;gap:12px}
  .brand__dot{width:40px;height:40px;border-radius:50%;background:var(--orange)}
  .brand__name{font-weight:800;font-size:30px;line-height:1;color:var(--ink);width:200px}
  .cover-title{position:absolute;left:20px;top:538px;font-family:"Oswald",sans-serif;font-size:58px;line-height:1;letter-spacing:-.5px}
  .cover-title b{font-weight:500;color:var(--ink)}
  .cover-title span{font-weight:300;color:var(--orange)}
  .cover-rule{position:absolute;left:20px;top:606px;width:74px;height:3px;background:var(--orange)}
  .contact{position:absolute;left:20px;top:632px;list-style:none;font-size:14px;color:#222;line-height:1.4}
  .contact li{display:flex;gap:10px;margin-bottom:8px;align-items:flex-start}
  .contact svg{flex:none;margin-top:2px}
  .call{position:absolute;left:315px;top:645px;display:flex;align-items:center;gap:12px;font-family:"Bebas Neue",sans-serif;font-size:34px;color:var(--orange)}
  .phone-box{position:absolute;left:315px;top:688px;width:204px;height:34px;background:#111;color:#fff;border-radius:4px;font-family:"Raleway",sans-serif;font-weight:700;font-size:27px;text-align:center;line-height:34px;letter-spacing:.5px}

  /* sheet */
  .title-bar{position:absolute;left:0;background:rgba(232,112,31,.88);font-family:"Bebas Neue",sans-serif;font-size:36px;color:#fff;padding-left:24px;line-height:42px}
  .title-bar--one{top:78px;width:226px}
  .title-bar--two{top:130px;width:242px}
  .section-head{position:absolute;left:20px;font-family:"Oswald",sans-serif;font-weight:500;font-size:25px;color:var(--orange-deep);letter-spacing:.3px}
  .intro-head{top:270px}
  .expertise-head{top:556px}
  .body-copy{position:absolute;left:20px;font-size:10.6px;line-height:15.4px;text-align:justify;color:var(--text)}
  .body-copy p{margin-bottom:11px}
  .intro-copy{top:316px;width:499px}
  .expertise-copy{top:600px;width:282px}
  .expertise-copy em{font-style:normal;color:var(--orange)}
  .expertise-photo{position:absolute;left:314px;top:567px;width:205px;height:137px;background:linear-gradient(180deg,#9fc3e6 0%,#c9d3dc 45%,#b89c7d 100%)}
  .expertise-photo::after{content:"";position:absolute;inset:6px 2px 8px 8px;border:1px solid rgba(255,255,255,.9)}
  .sheet-url{position:absolute;left:0;right:0;top:730px;text-align:center;font-size:11px;color:#333}
</style>
</head>
<body>

<section class="page page--cover">
  <svg class="page__art" viewBox="0 0 539 762" width="539" height="762">
    <defs>
      <linearGradient id="aerial" x1="0" y1="0" x2="1" y2="1">
        <stop offset="0" stop-color="#8b9a7c"/>
        <stop offset=".5" stop-color="#9aa0a6"/>
        <stop offset="1" stop-color="#5d6470"/>
      </linearGradient>
      <linearGradient id="sweep" x1="0" y1="0" x2="0" y2="1">
        <stop offset="0" stop-color="#f08a2a"/>
        <stop offset="1" stop-color="#e06a1c"/>
      </linearGradient>
    </defs>
    <path d="M330 0 H539 V400 C480 470 320 545 0 530 V512 C250 520 410 430 460 270 C495 160 430 60 330 0 Z" fill="url(#sweep)"/>
    <path role="img" aria-label="Aerial photo of an office building with rooftop solar panels" d="M0 218 C160 196 330 238 398 300 C350 410 210 492 0 512 Z" fill="url(#aerial)"/>
    <path d="M440 370 C495 420 528 480 539 530" fill="none" stroke="var(--orange)" stroke-width="6"/>
  </svg>
  <div class="brand">
    <span class="brand__dot"></span>
    <span class="brand__name">Vantrel Energy Solutions</span>
  </div>
  <h1 class="cover-title"><b>COMPANY</b> <span>OVERVIEW</span></h1>
  <div class="cover-rule"></div>
  <ul class="contact">
    <li><svg width="14" height="16" viewBox="0 0 14 16"><path d="M7 0a6 6 0 0 0-6 6c0 4.5 6 10 6 10s6-5.5 6-10a6 6 0 0 0-6-6zm0 8.5A2.5 2.5 0 1 1 7 3.5a2.5 2.5 0 0 1 0 5z" fill="#222"/></svg><span>418 MERIDIAN AVE SUITE<br>2200, DALLAS, TEXAS 75204</span></li>
    <li><svg width="14" height="12" viewBox="0 0 14 12"><rect x="0" y="1" width="14" height="10" fill="#222"/><path d="M0 1 L7 7 L14 1" fill="none" stroke="#fff" stroke-width="1.2"/></svg><span>info@vantrelenergy-example.com</span></li>
    <li><svg width="14" height="14" viewBox="0 0 14 14"><circle cx="7" cy="7" r="6" fill="none" stroke="#222" stroke-width="1.4"/><ellipse cx="7" cy="7" rx="2.6" ry="6" fill="none" stroke="#222" stroke-width="1.2"/><path d="M1 7h12M2 4h10M2 10h10" stroke="#222" stroke-width="1"/></svg><span>www.vantrelenergy-example.com</span></li>
  </ul>
  <div class="call">
    <svg width="34" height="34" viewBox="0 0 34 34"><path d="M8 4l5 7-3 3c2 4 5 7 9 9l3-3 7 5-3 5C16 30 4 18 3 7z" fill="var(--orange)"/><path d="M20 6a9 9 0 0 1 8 8M20 1a14 14 0 0 1 13 13" fill="none" stroke="var(--orange)" stroke-width="2.4"/></svg>
    <span>CALL US NOW!</span>
  </div>
  <div class="phone-box">555.014.2290</div>
  <div class="page__foot"></div>
</section>
<div class="page-label" style="left:256px">Page 1</div>

<section class="page page--sheet">
  <svg class="page__art" viewBox="0 0 539 762" width="539" height="762">
    <defs>
      <linearGradient id="field" x1="0" y1="0" x2="1" y2="1">
        <stop offset="0" stop-color="#b9a78e"/>
        <stop offset=".5" stop-color="#4a5f86"/>
        <stop offset="1" stop-color="#a89579"/>
      </linearGradient>
      <linearGradient id="roof" x1="0" y1="0" x2="0" y2="1">
        <stop offset="0" stop-color="#a9c2d8"/>
        <stop offset=".5" stop-color="#5b6f8e"/>
        <stop offset="1" stop-color="#8a8a88"/>
      </linearGradient>
    </defs>
    <path role="img" aria-label="Aerial photo of a large ground-mounted solar farm" d="M0 0 H539 V30 C480 160 330 230 0 250 Z" fill="url(#field)"/>
    <path d="M539 20 C480 160 330 235 0 255 V270 C330 248 490 170 539 60 Z" fill="var(--orange)"/>
    <circle cx="378" cy="178" r="100" fill="var(--orange)"/>
    <circle role="img" aria-label="Photo of a rooftop solar installation in a city" cx="378" cy="178" r="91" fill="url(#roof)"/>
  </svg>
  <h2 class="title-bar title-bar--one">STATEMENT OF</h2>
  <h2 class="title-bar title-bar--two">QUALIFICATIONS</h2>

  <h3 class="section-head intro-head">INTRODUCTION</h3>
  <div class="body-copy intro-copy">
    <p>Vantrel Energy Solutions and the Vantrel Group, family of companies, provide renewable energy solutions &amp; services. We specialize in developing, financing, constructing, owning &amp; operating solar and wind energy generation facilities. Facilities which range from small distributed generation to utility scale projects located across North America &amp; the Pacific Islands. At Vantrel Energy Solutions, we believe in creating power from sustainable, clean resources that will benefit our communities.</p>
    <p>With the global push towards cleaner &amp; more efficient ways of producing electricity, Vantrel Energy Solutions has come to the forefront of the industry to lead the charge. Our company's experience, innovative approach, business partners, &amp; sponsorship have caused a growth that can only be measured by leaps &amp; bounds.</p>
    <p>With segregations in the market, the founding members of Vantrel Energy Solutions saw a need to create a conglomerate. By affectively bringing all of the parties involved in a renewable energy project under one umbrella, Vantrel Energy Solutions can take a project from its inception to operation in the most efficient approach possible</p>
  </div>

  <h3 class="section-head expertise-head">EXPERTISE</h3>
  <div class="body-copy expertise-copy">
    <p>The founding members of Vantrel Energy Solutions have over 40 combined years in the industry. In that time, our record has been flawless in bringing projects to fruition. Our employees are specialty-trained for the benefit of our clients &amp; those looking to benefit from clean energy. We are focused on <em>value</em>, <em>safety</em>, &amp; <em>sustainability</em>.</p>
  </div>
  <div class="expertise-photo" role="img" aria-label="Photo of rows of solar panel mounts under a blue sky"></div>

  <div class="sheet-url">www.vantrelenergy-example.com</div>
  <div class="page__foot"></div>
</section>
<div class="page-label" style="left:866px">Page 2</div>

</body>
</html>
```